Exciting, Bold and Modern Landscaping & Turf care company business card

Hello, I own a lawn and landscaping company in Virginia, USA. We would like to design a bold, dynamic, modern business card that really makes us stand out. I tire of all green business cards with crappy, cartoonish clipart grass on them. It needs to be two sided, on one side i need to highlight our turf care division called "Promised Brighter Meadow" We maintain grass, fertilize it, weed control, etc.. We have a green thumbed gopher as our logo that i will attach. I am looking for something, clean and neat but out of the box in style. Im open to all ideas, and would like different options for them. On the other side, i want to highlight our landscaping division "Quiet Harbor Landscaping" In this division we design and install landscapes. Feel free to visit our website for more info or email me with ANY questions. Our busines cards in the past have highlighted our different services, but i don't want to this time. By the time I hand out a business card we are usually already estimating a project and they know what services we offer. I do want them to look at my card and say "wow thats pretty cool" and for them to think "These guys are something different, not just your standard dirt diggers" The logo doesnt have to be on both sides, but it needs to be on the turf care side. Our phone number and website should also be on at least on side, but need not be on both. The phone number is (555)618-4072 as well as the web address as www.MossbrookYardWorks.example. I like for the web address to have caps like that becasue it makes the long address much easier to read. I would like it in full color, printing costs are not my major concern. I also love rounded corners or interesting die cut designs as well, so feel free to wow me. Whether it be a clean white background with a bold photo to an all black card with a gray logo except for his green thumb with silver foil lettering to anything in between, lets go for it. That bieng said i dont want anything cartoonish, we are still a professional service and i want that to come through. THANKS!
Updates
Project Deadline Extended
Reason: changed project to a committed payment. I would like designers to re-evaluate their interest now and give them extra time to submit designs. Thank you.
we have changed our status to a commited payment to entice more submissions. thank you all for your hard work!
Industry/Entity Type
Professional Service
Look and feel
Each slider illustrates characteristics of the customer's brand and the style your logo design should communicate.

```html
<!DOCTYPE html>
<html lang="en">
<head>
<meta charset="utf-8">
<title>Quiet Harbor Landscaping – Business Cards</title>
<link rel="stylesheet" href="https://fonts.googleapis.com/css2?family=Cabin:wght@400;600;700&display=swap">
<style>
  :root {
    --backdrop: #3b3b3b;
    --card: #ffffff;
    --leaf: #6a9a1f;
    --turf: #1f6b3f;
    --ink: #1a1a1a;
    --meadow-light: #a9cf4a;
    --meadow-dark: #3f6a1c;
    --tree: #2d4a22;
    --fur-light: #e9a865;
    --fur: #c8762c;
    --grass: #5aa52e;
  }
  * { box-sizing: border-box; margin: 0; padding: 0; }
  html, body {
    width: 1200px;
    height: 949px;
    overflow: hidden;
    background: var(--backdrop);
    font-family: "Cabin", sans-serif;
  }
  .sheet {
    width: 1200px;
    height: 949px;
    display: flex;
    align-items: center;
    justify-content: center;
    gap: 40px;
  }
  .card {
    position: relative;
    width: 540px;
    height: 309px;
    background: var(--card);
    overflow: hidden;
    box-shadow: 0 6px 18px rgba(0,0,0,0.45);
  }

  /* Landscaping side */
  .landscape-side .contact {
    position: absolute;
    top: 40px;
    right: 44px;
    text-align: right;
    color: var(--ink);
  }
  .landscape-side .company {
    color: var(--leaf);
    font-weight: 700;
    font-size: 20px;
  }
  .landscape-side .address {
    font-size: 14px;
    line-height: 1.3;
    margin-top: 4px;
  }
  .landscape-side .phone {
    display: inline-flex;
    align-items: center;
    gap: 8px;
    font-size: 22px;
    margin-top: 6px;
  }
  .landscape-side .phone svg { width: 22px; height: 22px; }
  .meadow-strip {
    position: absolute;
    left: 0;
    bottom: 0;
    width: 100%;
    height: 78px;
    background:
      linear-gradient(to right, rgba(255,255,255,0) 0%, rgba(255,255,255,0) 42%, #fff 72%),
      linear-gradient(to bottom, #ffffff 0%, var(--tree) 32%, var(--meadow-dark) 48%, var(--meadow-light) 100%);
  }

  /* Turf care side */
  .turf-side .mascot {
    position: absolute;
    left: 10px;
    top: 22px;
    width: 230px;
    height: 287px;
    border-radius: 14px 14px 0 0;
    background: linear-gradient(160deg, var(--fur-light) 0%, var(--fur) 100%);
    overflow: hidden;
  }
  .turf-side .mascot::after {
    content: "";
    position: absolute;
    left: 0;
    bottom: 0;
    width: 100%;
    height: 16px;
    background: var(--grass);
  }
  .turf-side .website {
    position: absolute;
    top: 18px;
    right: 36px;
    font-size: 12px;
    color: var(--ink);
  }
  .turf-side .website strong { font-weight: 700; }
  .turf-side .tagline {
    position: absolute;
    top: 37px;
    left: 252px;
    right: 0;
    height: 54px;
    background: var(--turf);
    color: #ffffff;
    font-weight: 700;
    font-size: 18px;
    display: flex;
    align-items: center;
    justify-content: center;
    box-shadow: inset 0 0 0 2px var(--turf), inset 0 0 0 4px #ffffff;
  }
  .turf-side .phone {
    position: absolute;
    top: 100px;
    left: 316px;
    color: var(--turf);
    font-size: 21px;
  }
</style>
</head>
<body>
  <main class="sheet">
    <section class="card landscape-side">
      <div class="contact">
        <p class="company">"Quiet Harbor Landscaping"</p>
        <p class="address">4870-212 Alder Ln. PMB 118<br>Fairview Bay, VA 20190</p>
        <p class="phone">(555)618-4072
          <svg viewBox="0 0 24 24" aria-hidden="true">
            <circle cx="12" cy="12" r="10.5" fill="none" stroke="#1a1a1a" stroke-width="1.6"/>
            <path d="M8.2 6.5c.5-.4 1.1-.3 1.4.2l1.2 1.9c.3.5.2 1-.2 1.4l-.7.6c.6 1.5 1.6 2.6 3 3.3l.6-.7c.4-.4 1-.5 1.4-.2l1.9 1.2c.5.3.6 1 .2 1.4l-.9 1c-.6.6-1.5.8-2.3.5-3.1-1.2-5.4-3.6-6.5-6.7-.3-.8-.1-1.7.5-2.3z" fill="#1a1a1a"/>
          </svg>
        </p>
      </div>
      <div class="meadow-strip" role="img" aria-label="Photo of a green field with a tree line"></div>
    </section>

    <section class="card turf-side">
      <div class="mascot" role="img" aria-label="Illustrated gopher mascot giving a green thumbs-up, standing in grass"></div>
      <p class="website">www.<strong>MossbrookYardWorks</strong>.example</p>
      <p class="tagline">"Promised Brighter Meadow"</p>
      <p class="phone">Phone: (555)618-4072</p>
    </section>
  </main>
</body>
</html>
```